Electrical company business card design.

Hi, were an electrical company in Auckland New Zealand called Quenra Ltd. We focus mainly on high end residential and commercial so the card would be targeted towards that.
The card will be for myself, i am the director of the company.
Name: Derek Polworth
Position: Director/electrician
Phone: 021 387 9142
Email: derek@quenra-example.co.nz
Location: Auckland
As for colors the the blue color in the logo is preferred, i also don't mind a black background option.
Target Market(s)
High end residential and commercial
Industry/Entity Type
Electrician
Contact Information for Business Card
Name: Derek Polworth Position: Director/Electrician Phone: 021 387 9142, Email: derek@quenra-example.co.nz, Location: Auckland

```html
<!DOCTYPE html>
<html lang="en">
<head>
<meta charset="utf-8">
<title>Quenra Ltd — Business Card</title>
<link href="https://fonts.googleapis.com/css2?family=Michroma&display=swap" rel="stylesheet">
<style>
  :root {
    --bg: #2a2b2d;
    --bg-deep: #1c1d1f;
    --blue: #0a7fd0;
    --blue-light: #0c9ce0;
    --blue-dark: #0d4fa6;
    --charcoal: #4a4d50;
    --slate: #4d5155;
    --paper: #ffffff;
    --off-white: #ebebeb;
    --sky-text: #2aa3e6;
  }
  * { margin: 0; padding: 0; box-sizing: border-box; }
  html, body {
    width: 1200px; height: 689px; overflow: hidden;
    background: radial-gradient(ellipse at 60% 40%, var(--bg), var(--bg-deep));
    font-family: "Michroma", sans-serif;
  }
  .canvas {
    position: relative; width: 1200px; height: 689px;
    display: flex; align-items: center; justify-content: center; gap: 48px;
  }
  .card {
    position: relative; width: 520px; height: 297px;
    border-radius: 18px; overflow: hidden;
    box-shadow: 0 18px 40px rgba(0,0,0,0.45);
  }

  /* Back card */
  .card--back { background: var(--slate); }
  .back__panel {
    position: absolute; left: 0; top: 0; width: 270px; height: 100%;
    background: linear-gradient(160deg, var(--blue-light) 0%, var(--blue) 50%, var(--blue-dark) 100%);
  }
  .back__brand {
    position: absolute; left: 290px; top: 108px; right: 16px;
    white-space: nowrap;
  }
  .wordmark {
    color: var(--off-white); font-size: 31px; letter-spacing: 0.5px; line-height: 1;
    white-space: nowrap;
  }
  .back__tagline {
    margin-top: 12px; color: var(--off-white); font-size: 8.4px; letter-spacing: 0.8px;
  }
  .back__sector {
    margin-top: 14px; color: var(--sky-text); font-size: 7px; letter-spacing: 0.8px;
  }

  /* Front card */
  .card--front { background: var(--paper); }
  .front__brand {
    position: absolute; left: 40px; top: 52px;
    display: flex; align-items: center; gap: 14px;
  }
  .brand-dot {
    width: 32px; height: 32px; border-radius: 50%; background: var(--blue);
  }
  .front__brand .wordmark { color: var(--charcoal); font-size: 40px; }
  .front__tagline {
    position: absolute; left: 86px; top: 108px;
    color: var(--charcoal); font-size: 10px; letter-spacing: 1.2px;
  }
  .front__person {
    position: absolute; left: 40px; top: 178px; white-space: nowrap;
  }
  .person__name { color: var(--blue); font-size: 16px; letter-spacing: 0.3px; }
  .person__role { margin-top: 7px; color: var(--charcoal); font-size: 8.5px; letter-spacing: 0.5px; }
  .front__divider {
    position: absolute; left: 300px; top: 168px; width: 1px; height: 58px; background: var(--blue);
  }
  .front__contact {
    position: absolute; left: 316px; top: 172px; list-style: none; white-space: nowrap;
  }
  .contact__item {
    display: flex; align-items: center; gap: 8px; color: var(--charcoal);
  }
  .contact__item--phone { font-size: 14px; }
  .contact__item--place { font-size: 10px; margin-top: 12px; }
  .contact__icon { width: 16px; height: 16px; flex: none; }
  .front__band {
    position: absolute; left: 0; bottom: 0; width: 100%; height: 10px;
    background: linear-gradient(90deg, var(--blue-dark), var(--blue-light));
  }
</style>
</head>
<body>
<main class="canvas">
  <section class="card card--back" aria-label="Card reverse">
    <div class="back__panel"></div>
    <div class="back__brand">
      <div class="wordmark">QUENRA</div>
      <div class="back__tagline">POWER MEETS PRECISION</div>
      <div class="back__sector">RESIDENTIAL AND COMMERCIAL</div>
    </div>
  </section>

  <section class="card card--front" aria-label="Card front">
    <div class="front__brand">
      <span class="brand-dot"></span>
      <span class="wordmark">QUENRA</span>
    </div>
    <div class="front__tagline">POWER MEETS PRECISION</div>

    <div class="front__person">
      <div class="person__name">DEREK POLWORTH</div>
      <div class="person__role">DIRECTOR/ELECTRICIAN</div>
    </div>

    <div class="front__divider"></div>

    <ul class="front__contact">
      <li class="contact__item contact__item--phone">
        <svg class="contact__icon" viewBox="0 0 16 16" aria-hidden="true">
          <circle cx="8" cy="8" r="8" fill="#0a7fd0"/>
          <path d="M5.2 4.2l1.4-.2.8 2-1 .8a5 5 0 0 0 2.8 2.8l.8-1 2 .8-.2 1.4c-.2.5-.8.8-1.4.7A7 7 0 0 1 4.5 5.6c-.1-.6.2-1.2.7-1.4z" fill="#fff"/>
        </svg>
        021 387 9142
      </li>
      <li class="contact__item contact__item--place">
        <svg class="contact__icon" viewBox="0 0 16 16" aria-hidden="true">
          <circle cx="8" cy="8" r="8" fill="#0a7fd0"/>
          <path d="M8 3.5a3 3 0 0 0-3 3c0 2.2 3 6 3 6s3-3.8 3-6a3 3 0 0 0-3-3z" fill="#fff"/>
          <circle cx="8" cy="6.5" r="1.1" fill="#0a7fd0"/>
        </svg>
        Auckland
      </li>
    </ul>

    <div class="front__band"></div>
  </section>
</main>
</body>
</html>
```